Tarvo Mosquito Repellent Oil made from 100% Essential Oils

I want someone to design a label for a product for me. Here are the details of the project.

Mosquito Project A: The project name is called Tarvo. It's a mixture of 100% Essential Oils (about 14 of them to be exact) into one bottle. The bottle sizes will start from 3 milliliters, 5 milliliters, 10 milliliters and 20 milliliters and 30 milliliters (1 fl. oz.)

I want the label to have the Tarvo logo. You will have to create this logo from scratch. I don't have a logo now.

Here are the requirements:
1.0 Logo for Tarvo
1.1 100% pure essential oils
1.2 Net (size of the bottle)

1.3 Ingredients:
1.3a Citronella Oil
1.3b Neem Oil
1.3c Lemon grass Oil
1.3d Eucalyptus Oil

2.0 Aroma: Spicy

3.0 Benefits: Repel mosquitoes

4.0 Mixes Well With:
4.1 Shea Butter
4.2 Olive Oil

5.0 Extraction Method: Steam Distilled from plant's leaves and twigs.

6.0 Barcode Label

7.0 Address: Tarvo Mosquito Oils, LLC. 4807 Orchard Mill Rd. McLean, VA 22847
7.1 Website: www.tarvobugcare.example

8.0 Suggested Use: For external use only. Rub in your hands and gently apply it to your hands, legs and around your neck and ears. Apply it to scent. When mixing with Shea Butter, use about 4 drops with 20 milliliters of Shea Butter. When mixing with Olive Oil, use about 4 drops with 20 milliliters of Olive Oil.

9.0 Natural essential oils are highly concentrated and should be used with care.

10.0 Caution: Keep out of reach of children. Avoid contact with eyes. If pregnant or lactating, consult your healthcare practitioner before using. Do not eat.

Attached is how the bottles will look like.

Thank you,

Dorn

Target Market(s)

Countries with high rate of malaria, a mosquito-borne diseases.

Industry/Entity Type

Product

Logo Text

Tarvo

Font styles to use
Sans Serif
Script

Colors
ec1f27
faa54b
33a6d7

Requirements
Must have
• A logo, a website, a label for all the different bottle sizes. I have attached a logo of the "Veyla" bug repellent, I like that, it's nice and simple.
Nice to have
• I don't know, think of something that will be nice to have.
Should not have
• I don't know.

```html
<!DOCTYPE html>
<html lang="en">
<head>
<meta charset="utf-8">
<title>Tarvo Mosquito Repellent Oil – Labels</title>
<link rel="stylesheet" href="https://fonts.googleapis.com/css2?family=Oswald:wght@400;600&family=Arimo:wght@400;700&display=swap">
<style>
  :root {
    --bg: #bdbdbd;
    --orange-deep: #ef5a24;
    --orange: #f7941d;
    --orange-light: #faa54b;
    --yellow: #ffe44d;
    --brand-red: #ec1f27;
    --ink-blue: #1f4e9c;
    --ink-dark: #2b1408;
    --white: #ffffff;
  }
  * { box-sizing: border-box; margin: 0; padding: 0; }
  html, body { width: 1200px; height: 1200px; overflow: hidden; }
  body {
    background: radial-gradient(circle at 50% 45%, #d2d2d2, var(--bg) 70%);
    display: flex;
    align-items: center;
    justify-content: center;
    gap: 60px;
  }
  .label {
    position: relative;
    width: 460px;
    height: 920px;
    overflow: hidden;
    background:
      linear-gradient(90deg, transparent 48%, rgba(255,240,120,.55) 50%, transparent 52%),
      linear-gradient(180deg, var(--yellow) 0%, var(--orange) 22%, var(--orange) 55%, var(--orange-deep) 85%, var(--orange) 100%);
    box-shadow: 0 10px 30px rgba(0,0,0,.18);
  }
  .label-art {
    position: absolute;
    inset: 0;
    background:
      radial-gradient(circle at 50% 48%, rgba(255,230,120,.75) 0 18%, rgba(255,170,60,.35) 26%, transparent 40%),
      radial-gradient(ellipse at 15% 30%, rgba(255,235,200,.35), transparent 40%),
      radial-gradient(ellipse at 90% 55%, rgba(255,235,200,.3), transparent 40%);
  }
  .front .brand {
    position: absolute;
    top: 380px;
    left: 0; right: 0;
    display: flex;
    align-items: center;
    justify-content: center;
    gap: 14px;
  }
  .brand-dot {
    width: 22px; height: 22px;
    border-radius: 50%;
    background: var(--brand-red);
  }
  .brand-name {
    font-family: "Oswald", sans-serif;
    font-weight: 600;
    font-size: 96px;
    letter-spacing: 2px;
    color: var(--white);
    text-transform: uppercase;
  }
  .product {
    position: absolute;
    top: 630px;
    left: 0; right: 0;
    text-align: center;
    font-family: "Oswald", sans-serif;
  }
  .product-name {
    font-size: 46px;
    font-weight: 400;
    color: var(--ink-blue);
    line-height: 1.05;
    transform: scaleX(.82);
  }
  .product-blend {
    font-size: 27px;
    color: var(--ink-dark);
    transform: scaleX(.82);
  }
  .product-net {
    margin-top: 14px;
    font-size: 22px;
    color: var(--ink-dark);
    letter-spacing: 1px;
  }
  .back .info {
    position: absolute;
    top: 34px;
    left: 34px; right: 34px;
    text-align: center;
    font-family: "Arimo", sans-serif;
    font-size: 15px;
    line-height: 1.36;
    color: var(--ink-dark);
  }
  .info-block + .info-block { margin-top: 16px; }
  .info-heading { color: var(--ink-blue); }
  .info-caution .info-heading { font-weight: 700; }
</style>
</head>
<body>
  <section class="label front">
    <div class="label-art" role="img" aria-label="Orange glow background with white lightning bolts"></div>
    <div class="brand">
      <span class="brand-dot"></span>
      <span class="brand-name">Tarvo</span>
    </div>
    <div class="product">
      <p class="product-name">MOSQUITO REPELLENT OIL</p>
      <p class="product-blend">100% PURE ESSENTIAL OILS</p>
      <p class="product-net">NET 30 ML (1 FL. OZ.)</p>
    </div>
  </section>

  <section class="label back">
    <div class="label-art" role="img" aria-label="Orange glow background"></div>
    <div class="info">
      <div class="info-block">
        <p class="info-heading">Ingredients:</p>
        <p>Citronella Oil, Neem Oil, Lemon grass Oil, Eucalyptus Oil, Aroma: Spicy, Benefits: Repel mosquitoes, Mixes Well With: Shea Butter, Olive Oil</p>
      </div>
      <div class="info-block">
        <p class="info-heading">Extraction Method:</p>
        <p>Steam Distilled from plant's leaves and twigs.</p>
      </div>
      <div class="info-block">
        <p class="info-heading">Address:</p>
        <p>Tarvo Mosquito Oils, LLC. 4807 Orchard Mill Rd.<br>McLean, VA 22847<br>www.tarvobugcare.example</p>
      </div>
      <div class="info-block">
        <p class="info-heading">Suggested Use:</p>
        <p>For external use only. Rub in your hands and gently apply it to your hands, legs and around your neck and ears. Apply it to scent. When mixing with Shea Butter, use about 4 drops with 20 milliliters of Shea Butter. When mixing with Olive Oil, use about 4 drops with 20 milliliters of Olive Oil.</p>
      </div>
      <div class="info-block">
        <p>Natural essential oils are highly concentrated and should be used with care.</p>
      </div>
      <div class="info-block info-caution">
        <p class="info-heading">Caution:</p>
        <p>Keep out of reach of children. Avoid contact with eyes. If pregnant or lactating, consult your healthcare practitioner before using. Do not eat.</p>
      </div>
      <div class="info-block">
        <p>100% Pure Essential Oils · Net 30 ml (1 fl. oz.)</p>
      </div>
    </div>
  </section>
</body>
</html>
```